Fatigued and Overloaded by COVID Messages? We need original illustrations to show that.

Everywhere you look there are messages about COVID. That is leading many people to feel fatigued and overloaded by the messages.

We surveyed U.S. adults March 20th - 24th, 2020 and measured message fatigue, information overload, perceived repetition, and perceived exaggeration. Here is how participants responded:

When it comes to coronavirus . . .
55% feel exhausted by all the messages.
54% feel overloaded by the amount of information.
51% feel that the messages are repetitive.
47% feel like messages exaggerate how bad it is.

In other words, almost half of U.S. adults show signs of message fatigue, information overload, perceived message repetition, and perceived message exaggeration.

We will continue to survey 400 adults every week for the next 16 weeks. Each time we will measure message fatigue, information overload, perceived repetition, and perceived exaggeration. We expect that it will increase over time.

What are we looking for? We need innovative and original illustrations that attempt to communicate these findings. The illustrations would visualize message fatigue, information overload, perceived message repetition, and perceived message exaggeration.

What sort of visual are we looking for? Our preference is for an original illustration (or set of illustrations). Our preference is for creative and powerful illustrations, but we are also open to the creative and well-executed infographics.

We need these images fast . We will award monetary prizes to the 3 best designs. If we like more than that, then we might purchase more (e.g., in past contests, we have purchased as many as 30 designs).

What we will need:
(1) The illustrations must be original and we will need the photoshop and/or illustrator files for all artwork. (By original, we mean that the illustrations are 100% created by you. Our organization requires that we utilize only original illustrated work. We have had issues with free imagery being pirated and reposted as free. We sidestep that issue by just having everything created.)

(2) The illustration should say, somewhere: "Based on a survey of 400 U.S. adults conducted March 20 - 24th, 2020."

(3) We will have almost 4 months worth of data by the time this is done. In other words, the illustrations might be able to help us present that weekly data.

(4) We have conducted other Artvendo projects. It might be helpful to examine designs we liked in the past. For example, here is another COVID project we just finished:

https://jobs.artvendo-example.com/job/5162048

Target Market(s)

U.S. adults

Requirements
Must have
• Original illustrations. Mobile friendly design. People will view this on their smartphones.
Nice to have
• A design that we can use to communicate the data across time.

```html
<!DOCTYPE html>
<html lang="en">
<head>
<meta charset="utf-8">
<title>Week 1 – When it comes to CoronaVirus</title>
<link rel="stylesheet" href="https://fonts.googleapis.com/css2?family=Roboto:ital,wght@0,300;0,400;0,500;0,700;1,700&family=Roboto+Slab:wght@700&display=swap">
<style>
  :root {
    --bg-top: #f3f4f6;
    --bg-bottom: #dadbde;
    --ink: #3a3d44;
    --muted: #6b6e75;
    --teal: #1ea597;
    --connector: #c9cbcf;
    --orange: #e5623a;
    --orange-soft: #f6c4b4;
    --mint: #5db8a8;
    --mint-soft: #cde9e3;
    --lime: #a5c83b;
    --lime-soft: #e2eec0;
    --sun: #f5cf1f;
    --sun-soft: #fbefb4;
    --pill-start: #3fb0e6;
    --pill-end: #2f8fd0;
    --white: #ffffff;
  }
  * { margin: 0; padding: 0; box-sizing: border-box; }
  html, body { width: 934px; height: 1200px; overflow: hidden; }
  body {
    font-family: "Roboto", Arial, sans-serif;
    background: linear-gradient(180deg, var(--bg-top), var(--bg-bottom));
    color: var(--ink);
  }
  .poster { position: relative; width: 934px; height: 1200px; }
  .diagram { position: absolute; inset: 0; }
  .week-label {
    position: absolute; left: 34px; top: 14px;
    font-size: 27px; font-weight: 300; letter-spacing: 1px; color: var(--muted);
  }
  .headline {
    position: absolute; left: 32px; top: 42px;
    font-size: 58px; font-weight: 400; color: var(--teal); line-height: 1;
    white-space: nowrap;
  }
  .headline .topic {
    font-family: "Roboto Slab", Georgia, serif; font-weight: 700; font-size: 56px;
  }
  .stat-label {
    position: absolute; font-size: 21px; line-height: 1.35; color: var(--ink);
  }
  .stat-label.overload { left: 34px; top: 206px; }
  .stat-label.exhausted { left: 583px; top: 196px; }
  .stat-label.repetitive { left: 34px; top: 758px; }
  .stat-label.exaggerate { left: 583px; top: 758px; }
  .stat-value {
    font-family: "Roboto", Arial, sans-serif; font-weight: 400; fill: var(--white);
    text-anchor: middle; dominant-baseline: central;
  }
  .summary-pill {
    position: absolute; left: 134px; top: 941px; width: 546px; height: 62px;
    border-radius: 31px;
    background: linear-gradient(90deg, var(--pill-start), var(--pill-end));
    color: var(--white); font-size: 30px; font-weight: 400; letter-spacing: 0.5px;
    display: flex; align-items: center; justify-content: center;
  }
  .summary-text {
    position: absolute; left: 110px; top: 1018px; width: 600px;
    text-align: center; font-size: 17px; font-weight: 500; line-height: 1.4; color: var(--ink);
  }
  .presenter-art {
    position: absolute; left: 700px; top: 910px; width: 168px; height: 212px;
    border-radius: 40px 40px 12px 12px;
    background: linear-gradient(180deg, #b9d6ea 0%, #c98e63 35%, #2f6fa8 70%, #1f4e7a 100%);
    opacity: 0.85;
  }
  .source-note {
    position: absolute; left: 0; width: 934px; top: 1158px;
    text-align: center; font-size: 17px; font-weight: 700; font-style: italic; color: var(--ink);
  }
</style>
</head>
<body>
<main class="poster">
  <svg class="diagram" width="934" height="1200" viewBox="0 0 934 1200" aria-hidden="false">
    <defs>
      <radialGradient id="virus-tone" cx="50%" cy="45%" r="55%">
        <stop offset="0%" stop-color="#c4202f"/>
        <stop offset="100%" stop-color="#6e0d17"/>
      </radialGradient>
      <radialGradient id="portrait-tone" cx="50%" cy="45%" r="60%">
        <stop offset="0%" stop-color="#f2c7a6"/>
        <stop offset="55%" stop-color="#8a5a35"/>
        <stop offset="100%" stop-color="#5fb3e0"/>
      </radialGradient>
    </defs>

    <!-- connectors -->
    <g class="connectors" stroke="var(--connector)" stroke-width="8" stroke-linecap="round">
      <line x1="449" y1="503" x2="449" y2="186"/>
      <line x1="449" y1="503" x2="205" y2="373"/>
      <line x1="449" y1="503" x2="205" y2="615"/>
      <line x1="449" y1="503" x2="466" y2="768"/>
      <line x1="449" y1="503" x2="699" y2="503"/>
    </g>

    <!-- 55% exhausted -->
    <g class="stat-ring exhausted">
      <circle cx="449" cy="186" r="58" fill="none" stroke="var(--orange-soft)" stroke-width="22"/>
      <circle cx="449" cy="186" r="58" fill="none" stroke="var(--orange)" stroke-width="22"
              pathLength="100" stroke-dasharray="55 100" transform="rotate(-90 449 186)"/>
      <circle cx="449" cy="186" r="58" fill="none" stroke="var(--white)" stroke-width="22"
              pathLength="100" stroke-dasharray="0.6 7.73" transform="rotate(-90 449 186)"/>
      <circle cx="449" cy="186" r="47" fill="var(--white)"/>
      <circle cx="449" cy="186" r="40" fill="var(--orange)"/>
      <text class="stat-value" x="449" y="187" font-size="30">55%</text>
    </g>

    <!-- 54% overloaded -->
    <g class="stat-ring overload">
      <circle cx="205" cy="373" r="74" fill="none" stroke="var(--mint-soft)" stroke-width="28"/>
      <circle cx="205" cy="373" r="74" fill="none" stroke="var(--mint)" stroke-width="28"
              pathLength="100" stroke-dasharray="54 100" transform="rotate(-90 205 373)"/>
      <circle cx="205" cy="373" r="74" fill="none" stroke="var(--white)" stroke-width="28"
              pathLength="100" stroke-dasharray="0.5 7.83" transform="rotate(-90 205 373)"/>
      <circle cx="205" cy="373" r="60" fill="var(--white)"/>
      <circle cx="205" cy="373" r="51" fill="var(--mint)"/>
      <text class="stat-value" x="205" y="374" font-size="32">54%</text>
    </g>

    <!-- 51% repetitive -->
    <g class="stat-ring repetitive">
      <circle cx="205" cy="615" r="74" fill="none" stroke="var(--lime-soft)" stroke-width="28"/>
      <circle cx="205" cy="615" r="74" fill="none" stroke="var(--lime)" stroke-width="28"
              pathLength="100" stroke-dasharray="51 100" transform="rotate(-90 205 615)"/>
      <circle cx="205" cy="615" r="74" fill="none" stroke="var(--white)" stroke-width="28"
              pathLength="100" stroke-dasharray="0.5 7.83" transform="rotate(-90 205 615)"/>
      <circle cx="205" cy="615" r="60" fill="var(--white)"/>
      <circle cx="205" cy="615" r="51" fill="var(--lime)"/>
      <text class="stat-value" x="205" y="616" font-size="32">51%</text>
    </g>

    <!-- 47% exaggerate -->
    <g class="stat-ring exaggerate">
      <circle cx="466" cy="768" r="74" fill="none" stroke="var(--sun-soft)" stroke-width="28"/>
      <circle cx="466" cy="768" r="74" fill="none" stroke="var(--sun)" stroke-width="28"
              pathLength="100" stroke-dasharray="47 100" transform="rotate(-90 466 768)"/>
      <circle cx="466" cy="768" r="74" fill="none" stroke="var(--white)" stroke-width="28"
              pathLength="100" stroke-dasharray="0.5 7.83" transform="rotate(-90 466 768)"/>
      <circle cx="466" cy="768" r="60" fill="var(--white)"/>
      <circle cx="466" cy="768" r="51" fill="var(--sun)"/>
      <text class="stat-value" x="466" y="769" font-size="32">47%</text>
    </g>

    <!-- central virus hub -->
    <g class="virus-hub">
      <circle cx="449" cy="503" r="93" fill="#b9bbc0"/>
      <circle cx="449" cy="503" r="80" fill="#e4e5e8"/>
      <circle cx="449" cy="503" r="62" fill="url(#virus-tone)" role="img"
              aria-label="Illustration of a red coronavirus particle"/>
    </g>

    <!-- portrait frame -->
    <g class="portrait">
      <circle cx="699" cy="503" r="186" fill="var(--white)" stroke="#9fd2f0" stroke-width="8"/>
      <circle cx="699" cy="503" r="160" fill="#7cc3ec"/>
      <circle cx="699" cy="503" r="140" fill="url(#portrait-tone)" role="img"
              aria-label="Illustration of a tired, sick young woman wearing a green scarf"/>
    </g>
  </svg>

  <div class="week-label">WEEK 1</div>
  <h1 class="headline">When it comes to <span class="topic">CoronaVirus</span>...</h1>

  <p class="stat-label overload">Feel overloaded by<br>the amount of information</p>
  <p class="stat-label exhausted">Feel exhausted<br>by all the messages</p>
  <p class="stat-label repetitive">Feel that the messages<br>are repetitive</p>
  <p class="stat-label exaggerate">Feel like messages<br>exaggerate how bad it is</p>

  <div class="summary-pill">WHAT DOES THIS DATA SAY</div>
  <p class="summary-text">Almost half of U.S. adults show signs of message fatigue,<br>information overload, perceived message repetition<br>and perceived message exaggeration</p>

  <div class="presenter-art" role="img" aria-label="Illustration of a man in a face mask and suit presenting the findings"></div>

  <p class="source-note">Based on a survey of 400 U.S. adults conducted March 20 - 24th, 2020</p>
</main>
</body>
</html>
```